TriVex Business Card Design - double sided -plumbing local plumbing company

We have a Plumbing company where the design was create through Sketch Hive. We would now like a business card designed as well. We want it to be in the colour version of the logo.

Details below for the card.

Phone Number: 0438 615 247
Email: info@trivexplumbing.example.au
Website: https://trivexplumbing.example.au
We really want a sophisticated design that stand out from the other- informative and timeless.

Target Market(s)

local Canberra market

Industry/Entity Type

Plumbing, gas fitting, hot water

Contact Information for Business Card

Phone number, email, logo and "Supplying all your heating, cooling and hot water needs"

Requirements
Must have
• bust be colourful, must also be though about it being printed on a magnet. must Vex with the logo - I dont want the logo and information chucked onto a white canvas I would prefer it to be smooth and look purposeful

```html
<!DOCTYPE html>
<html lang="en">
<head>
<meta charset="utf-8">
<title>TriVex Business Card</title>
<link href="https://fonts.googleapis.com/css2?family=Lato:wght@400;700;900&display=swap" rel="stylesheet">
<style>
  :root {
    --brand-blue: #03aeef;
    --brand-orange: #fbb040;
    --brand-navy: #031f3a;
    --paper: #ffffff;
    --backdrop: #f4f4f4;
  }
  html, body {
    margin: 0;
    padding: 0;
    width: 1034px;
    height: 1200px;
    overflow: hidden;
    background: var(--backdrop);
    font-family: "Lato", sans-serif;
  }
  .canvas {
    position: relative;
    width: 1034px;
    height: 1200px;
  }
  .card {
    position: absolute;
    left: 133px;
    width: 820px;
    height: 469px;
    background: var(--paper);
    overflow: hidden;
    transform: scale(0.94);
    transform-origin: top left;
  }
  .card--front { top: 112px; }
  .card--back { top: 648px; }

  .wordmark {
    position: absolute;
    margin: 0;
    font-family: "Lato", sans-serif;
    font-weight: 900;
    font-size: 118px;
    line-height: 1;
    letter-spacing: 2px;
    color: var(--brand-blue);
  }
  .card--front .wordmark { left: 28px; top: 40px; }

  .wave { position: absolute; left: 0; top: 0; width: 820px; height: 469px; }

  .holder {
    position: absolute;
    right: 37px;
    top: 206px;
    text-align: right;
  }
  .holder__name {
    margin: 0;
    font-weight: 700;
    font-size: 40px;
    line-height: 1;
    color: var(--brand-blue);
  }
  .holder__role {
    margin: 8px 9px 0 0;
    font-weight: 400;
    font-size: 23px;
    line-height: 1;
    color: var(--brand-orange);
  }

  .contact {
    position: absolute;
    left: 50px;
    top: 266px;
    margin: 0;
    padding: 0;
    list-style: none;
    color: var(--paper);
    font-size: 22px;
  }
  .contact__item {
    display: flex;
    align-items: center;
    height: 30px;
  }
  .contact__icon { width: 20px; height: 20px; margin-right: 11px; flex: none; }

  .address {
    position: absolute;
    left: 52px;
    top: 372px;
    margin: 0;
    font-style: normal;
    color: var(--paper);
    font-size: 19px;
    line-height: 23px;
  }

  .band {
    position: absolute;
    left: 0;
    top: 142px;
    width: 820px;
    height: 186px;
    background: var(--brand-navy);
  }
  .card--back .wordmark {
    left: 0;
    width: 820px;
    top: 174px;
    text-align: center;
  }
  .tagline {
    position: absolute;
    left: 0;
    top: 344px;
    width: 820px;
    margin: 0;
    text-align: center;
    font-weight: 700;
    font-size: 21px;
    color: var(--brand-navy);
  }
</style>
</head>
<body>
<main class="canvas">

  <section class="card card--front" aria-label="Business card front">
    <svg class="wave" viewBox="0 0 820 469" aria-hidden="true">
      <path fill="var(--brand-orange)" d="M0,222 C110,186 240,194 335,244 L335,250 C230,206 110,204 0,238 Z"/>
      <path fill="var(--brand-orange)" d="M495,318 C600,366 710,380 820,346 L820,364 C710,396 600,382 495,318 Z"/>
      <path fill="var(--brand-blue)" d="M0,254 C100,208 232,212 342,264 C452,318 560,370 680,384 C740,390 790,384 820,379 L820,469 L0,469 Z"/>
    </svg>

    <h1 class="wordmark">TriVex</h1>

    <div class="holder">
      <p class="holder__name">Kael Norwin</p>
      <p class="holder__role">President</p>
    </div>

    <ul class="contact">
      <li class="contact__item">
        <svg class="contact__icon" viewBox="0 0 20 20" aria-hidden="true">
          <path fill="#fff" d="M5 2 L8 6 L6.5 8 C7.5 10.5 9.5 12.5 12 13.5 L14 12 L18 15 L16 18 C9 18 2 11 2 4 Z"/>
        </svg>
        <span>0438 615 247</span>
      </li>
      <li class="contact__item">
        <svg class="contact__icon" viewBox="0 0 20 20" aria-hidden="true">
          <rect x="2" y="5" width="16" height="11" fill="none" stroke="#fff" stroke-width="1.6"/>
          <path d="M2 5 L10 11 L18 5" fill="none" stroke="#fff" stroke-width="1.6"/>
        </svg>
        <span>info@trivexplumbing.example.au</span>
      </li>
      <li class="contact__item">
        <svg class="contact__icon" viewBox="0 0 20 20" aria-hidden="true">
          <circle cx="10" cy="10" r="8" fill="none" stroke="#fff" stroke-width="1.6"/>
          <ellipse cx="10" cy="10" rx="3.5" ry="8" fill="none" stroke="#fff" stroke-width="1.4"/>
          <path d="M2 10 H18" stroke="#fff" stroke-width="1.4"/>
        </svg>
        <span>https://trivexplumbing.example.au</span>
      </li>
    </ul>

    <address class="address">
      Harbour Line Supply Works<br>
      Unit 7&nbsp; B 4410 Ridgeway Drive
    </address>
  </section>

  <section class="card card--back" aria-label="Business card back">
    <div class="band"></div>
    <h2 class="wordmark">TriVex</h2>
    <p class="tagline">"Supplying all your heating, cooling and hot water needs"</p>
  </section>

</main>
</body>
</html>
```